Label/sheets for packaging/boxing

We need a label to go on our shipping boxes. Also a time to reorder label or card to put into boxes. We want to use this in different sizes. I want our logo, which we will provide to be used on all items.I would like a flag and eagle ( I will provide file) to be graduated screen tint in upper left or the left side and my company logo and information to be on top solid.....or any design that is better than this idea...I would like the label 4x2.5 inched landscape......I would like to use the file to print different size labels.
Really, the design can be anything using my logo........I'm open for design.
Also, a time to re-order card or label with logo and info, it can include a thank you for ordering from us................confidence, etc. I really want this to stand out and look great.
Updates

Project Deadline Extended
Reason: We are able to add more time to project. Thanks.

Target Market(s)

Business, City accounts.

Industry/Entity Type

Shipping

Requirements
Must have
• Name address contact information, web address....ect.

Eco friendly....
Professional

```html
<!DOCTYPE html>
<html lang="en">
<head>
<meta charset="utf-8">
<title>Shipping Label</title>
<link rel="stylesheet" href="https://fonts.googleapis.com/css2?family=Courier+Prime:wght@700&family=Archivo+Black&display=swap">
<style>
  :root {
    --kraft: #d8b387;
    --paper: #fbfbf9;
    --navy: #123a6d;
    --crimson: #9c0f3b;
    --line-navy: #4a6d9b;
    --line-crimson: #b5476b;
    --flag-red: #b8202f;
    --flag-blue: #1e2f63;
    --eagle-dark: #2b2b2b;
  }
  * { box-sizing: border-box; margin: 0; padding: 0; }
  html, body { width: 1200px; height: 848px; overflow: hidden; }
  body {
    background: var(--kraft);
    display: flex;
    align-items: center;
    justify-content: center;
  }
  .label {
    position: relative;
    width: 640px;
    height: 400px;
    background: var(--paper);
    border-radius: 28px;
    overflow: hidden;
    box-shadow: 0 0 0 10px #ffffff;
  }
  .hero-art {
    position: absolute;
    left: 0; top: 0;
    width: 330px; height: 100%;
    background:
      linear-gradient(90deg, rgba(251,251,249,0) 55%, var(--paper) 100%),
      linear-gradient(180deg, var(--flag-blue) 0%, #7d3a52 30%, #d9d5d0 55%, var(--eagle-dark) 100%);
  }
  .eco-badge {
    position: absolute;
    left: 26px; bottom: 34px;
    width: 64px; height: 58px;
    background: var(--crimson);
    display: flex; align-items: center; justify-content: center;
  }
  .color-edge {
    position: absolute;
    right: 0; top: 0;
    width: 62px; height: 100%;
    background: linear-gradient(180deg, #f5d23c 0%, #f39a2b 18%, #ec5f9c 40%, #a36bd1 60%, #6f8ddc 78%, #2db6d8 100%);
    opacity: .85;
    -webkit-mask: linear-gradient(90deg, transparent 0%, #000 70%);
            mask: linear-gradient(90deg, transparent 0%, #000 70%);
  }
  .brand {
    position: absolute;
    left: 370px; top: 56px;
    display: flex; align-items: center; gap: 12px;
  }
  .brand-mark {
    width: 30px; height: 30px;
    background: var(--crimson);
  }
  .brand-name {
    font-family: 'Archivo Black', sans-serif;
    font-size: 30px;
    color: var(--navy);
    line-height: 1;
    letter-spacing: .5px;
  }
  .contact-fields {
    position: absolute;
    left: 360px; top: 175px;
    width: 215px;
    list-style: none;
    font-family: 'Courier Prime', monospace;
    font-weight: 700;
    font-size: 15px;
  }
  .field {
    display: flex;
    align-items: flex-end;
    gap: 8px;
    height: 24px;
    color: var(--navy);
  }
  .field::after {
    content: "";
    flex: 1;
    border-bottom: 1px solid var(--line-navy);
    margin-bottom: 4px;
  }
  .field--spacer { height: 28px; }
  .field--spacer::after { margin-left: 0; }
  .field--accent { color: var(--crimson); }
  .field--accent::after { border-color: var(--line-crimson); }
</style>
</head>
<body>
  <div class="label">
    <div class="hero-art" role="img" aria-label="American flag waving behind a bald eagle, fading into the label"></div>
    <div class="eco-badge">
      <svg width="34" height="34" viewBox="0 0 34 34" aria-label="Recycle symbol" role="img">
        <g fill="none" stroke="#fff" stroke-width="3" stroke-linecap="round">
          <path d="M9 24 A10 10 0 0 1 12 8"/>
          <path d="M17 6 A10 10 0 0 1 27 19"/>
          <path d="M24 26 A10 10 0 0 1 11 27"/>
        </g>
        <g fill="#fff">
          <polygon points="9,5 16,8 11,13"/>
          <polygon points="30,16 26,23 22,17"/>
          <polygon points="12,31 8,24 15,24"/>
        </g>
      </svg>
    </div>
    <div class="color-edge" role="img" aria-label="Colourful crayon strokes along the right edge"></div>

    <div class="brand">
      <span class="brand-mark"></span>
      <span class="brand-name">Ridgeline Print</span>
    </div>

    <ul class="contact-fields">
      <li class="field">Name</li>
      <li class="field">Address</li>
      <li class="field field--spacer"></li>
      <li class="field">Phone</li>
      <li class="field">Mobile</li>
      <li class="field field--accent">Web</li>
      <li class="field field--accent">Email</li>
    </ul>
  </div>
</body>
</html>
```